Wes Hadley Golf Teaching Rack Card

The flyer will be a rack card. Front side only. Nothing on back. 3.75 inches by 8.5 inches. Or close to that. I’d like it to be as colorful as possible and to include several logos in different places.
The brochure is to attract golfers attention and still look traditional and classy not crazy or to artsy. Golf is a very traditional sport and would just like it to look professional and welcoming so golfers no I’m credible in my teaching and they will learn something. I will send a rough idea and a sample of one I had before but use your creative skills and ingenuity to design it. You will have to put my name: Wes Hadley under the NLT logo. It is a requirement by the NLT. Also the logo size must me .0875 inches high. If possible use a gotham or Hoefler text type or something businesslike or similar for my name. Also I am sorry for the different logos available on this file because I am not tech savvy so you will have to choose the best logo and cut it out of the grouping to match what you want to do. I am sorry for all the details. I will be available all weekend if you need more info. or help. I am sure you are very skilled and can tell I am not. Sorry. I laid out a sketch for you so you know what info. verbiage is important. and where to somewhat place the logos. Up to your skill for most of it. Your design! Go for it.!

Target Market(s)

Golfers of all ages from 18-70. Men and Women.

Industry/Entity Type

Golf Industry. Teaching and learning game if golf

Font styles to use
Sans Serif
Other font styles liked:
• Mixture maybe traditional type. Easy to read.

Colors

Designer to choose only greyscale colors for use in the design.

Requirements
Must have
• My WHG golf logo and the NLT official logo. Also will send several other logos to put in. I will tell you where they should go on the rack card.
Nice to have
• Maybe a golf picture from a course with a green and flag as the one on my old brochure I’m sending or similar. It just adds color and eye catching
Should not have
• Nothing hard to read or difficult to comprehend. Pretty straight forward and quality and style in a traditional sense,

```html
<!DOCTYPE html>
<html lang="en">
<head>
<meta charset="utf-8">
<title>Wes Hadley Golf – Rack Card</title>
<link rel="stylesheet" href="https://fonts.googleapis.com/css2?family=Oswald:wght@300;400;500;700&family=Raleway:ital,wght@0,400;0,500;0,600;1,400&display=swap">
<style>
  :root{
    --page:#dcdcdc;
    --white:#ffffff;
    --text-dark:#333333;
    --band-dark:#3a3a3a;
    --panel:#5e5e5e;
    --rule:#a6a6a6;
    --accent:#8a8a8a;
    --accent-light:#c4c4c4;
    --disc-ring:#bdbdbd;
    --price:#262626;
    --tag-left:#585858;
    --tag-right:#474747;
    --partner-one:#7a7a7a;
    --ink:#1e1e1e;
    --note:#d4d4d4;
    --tick:#d0d0d0;
  }
  *{margin:0;padding:0;box-sizing:border-box}
  html,body{width:848px;height:1200px;overflow:hidden;background:var(--page)}
  .card{position:absolute;left:172px;top:28px;width:504px;height:1144px;overflow:hidden;background:var(--white);font-family:'Raleway',sans-serif}
  .card-art{position:absolute;inset:0}
  .abs{position:absolute}
  .brand-name{right:34px;top:92px;width:220px;text-align:right;font-family:'Raleway',sans-serif;font-weight:600;color:var(--text-dark);font-size:26px;line-height:30px}
  .contact{right:34px;top:177px;text-align:right;font-family:'Oswald',sans-serif;font-weight:500;color:var(--text-dark);font-size:19px;line-height:30px;text-shadow:0 0 4px #fff,0 0 2px #fff}
  .hero-title{left:131px;top:256px;width:240px;text-align:center;font-family:'Oswald',sans-serif;font-weight:700;color:var(--white);font-size:40px;line-height:41px}
  .hero-price{left:131px;top:396px;width:240px;text-align:center;font-family:'Oswald',sans-serif;font-weight:700;color:var(--price);font-size:52px;line-height:56px}
  .hero-price sup{font-size:22px;vertical-align:top;line-height:40px}
  .tag-hour{left:45px;top:380px;width:120px;text-align:center;font-family:'Oswald',sans-serif;font-weight:300;color:var(--white);font-size:20px;line-height:23px}
  .tag-offer{left:342px;top:364px;width:116px;text-align:center;font-family:'Oswald',sans-serif;font-weight:300;color:var(--white);font-size:14px;line-height:17px}
  .tag-offer strong{display:block;font-weight:700;font-size:23px;line-height:23px;margin-top:3px}
  .tag-offer sup{font-size:11px;vertical-align:top;line-height:16px}
  .includes-title{left:0;width:504px;text-align:center;letter-spacing:6px;color:var(--accent);font-size:18px;font-weight:500}
  .feature-list{left:0;top:510px;width:504px;list-style:none;text-align:center;color:var(--text-dark);font-size:15.5px;line-height:26px}
  .feature-list li::before{content:"";display:inline-block;width:3px;height:13px;background:var(--accent);margin-right:7px;vertical-align:-1px;box-shadow:-5px 0 0 var(--accent-light)}
  .info-cell{left:40px;width:205px;text-align:center;color:var(--text-dark);font-size:15.5px;line-height:19px}
  .info-cell b{font-weight:600}
  .partner{left:262px;width:200px;text-align:center;font-family:'Raleway',sans-serif;font-weight:600;font-size:33px;line-height:40px}
  .partner-swing{top:639px;color:var(--partner-one)}
  .partner-track{top:701px;color:var(--ink)}
  .ribbon-text{left:80px;top:788px;width:342px;text-align:center;font-family:'Oswald',sans-serif;font-weight:700;color:var(--ink);font-size:28px;line-height:40px}
  .package-line{left:0;top:841px;width:504px;text-align:center;font-family:'Oswald',sans-serif;color:var(--white);font-size:18px}
  .package-line sup{font-size:9px;vertical-align:top;line-height:14px}
  .package-line .sep{opacity:.7;margin:0 10px}
  .package-price{left:0;top:871px;width:504px;text-align:center;color:var(--white)}
  .package-price .amt{font-family:'Oswald',sans-serif;font-weight:700;font-size:42px}
  .package-price .amt sup{font-size:20px;vertical-align:top;line-height:36px}
  .package-price .note{font-style:italic;font-size:17px;margin-left:4px}
  .package-sub{top:932px;color:var(--white);font-size:13px;letter-spacing:5px;font-weight:400}
  .package-list{left:0;top:955px;width:504px;list-style:none;text-align:center;color:var(--white);font-size:14.5px;line-height:17px}
  .package-list li{margin-bottom:9px}
  .package-list li::before{content:"\2713";color:var(--tick);margin-right:5px}
  .footer-note{left:0;top:1092px;width:504px;text-align:center;color:var(--note);font-style:italic;font-size:10.5px;line-height:15px}
</style>
</head>
<body>
<main class="card">
  <svg class="card-art" width="504" height="1144" viewBox="0 0 504 1144">
    <defs>
      <linearGradient id="scene" x1="0" y1="0" x2="0" y2="1">
        <stop offset="0" stop-color="#d9d9d9"/>
        <stop offset="0.45" stop-color="#ececec"/>
        <stop offset="0.7" stop-color="#a9a9a9"/>
        <stop offset="1" stop-color="#8a8a8a"/>
      </linearGradient>
      <radialGradient id="disc" cx="0.5" cy="0.4" r="0.6">
        <stop offset="0" stop-color="#9c9c9c"/>
        <stop offset="1" stop-color="#777777"/>
      </radialGradient>
      <linearGradient id="ribbon" x1="0" y1="0" x2="1" y2="0">
        <stop offset="0" stop-color="#9a9a9a"/>
        <stop offset="0.5" stop-color="#e8e8e8"/>
        <stop offset="1" stop-color="#9a9a9a"/>
      </linearGradient>
      <radialGradient id="shadow" cx="0.5" cy="0.5" r="0.5">
        <stop offset="0" stop-color="#000" stop-opacity=".12"/>
        <stop offset="1" stop-color="#000" stop-opacity="0"/>
      </radialGradient>
    </defs>
    <rect class="course-photo" x="0" y="0" width="504" height="440" fill="url(#scene)" role="img" aria-label="Photo of a golfer finishing his swing on a sunlit course"/>
    <path d="M0,428 Q252,330 504,428 L504,1144 L0,1144 Z" fill="var(--white)"/>
    <ellipse cx="105" cy="472" rx="70" ry="12" fill="url(#shadow)"/>
    <ellipse cx="400" cy="472" rx="70" ry="12" fill="url(#shadow)"/>
    <path d="M0,729 Q252,835 504,717 L504,1144 L0,1144 Z" fill="var(--band-dark)"/>
    <rect x="43" y="806" width="417" height="278" fill="var(--panel)"/>
    <line x1="43" y1="807" x2="460" y2="807" stroke="var(--rule)" stroke-width="3"/>
    <polygon points="80,781 422,781 408,808 422,834 80,834 94,808" fill="url(#ribbon)"/>
    <circle cx="105" cy="404" r="60" fill="var(--tag-left)"/>
    <circle cx="400" cy="404" r="58" fill="var(--tag-right)"/>
    <circle cx="251" cy="354" r="122" fill="var(--disc-ring)"/>
    <circle cx="251" cy="354" r="115" fill="url(#disc)"/>
    <line x1="166" y1="389" x2="336" y2="389" stroke="#d6d6d6" stroke-width="1.5"/>
    <line x1="251" y1="638" x2="251" y2="745" stroke="var(--rule)" stroke-width="1.2"/>
    <line x1="50" y1="692" x2="453" y2="692" stroke="var(--rule)" stroke-width="1.2"/>
    <path d="M136,875 q-8,0 -8,10 v10 q0,6 -6,6 q6,0 6,6 v10 q0,10 8,10" fill="none" stroke="#3f3f3f" stroke-width="1.5"/>
    <path d="M368,875 q8,0 8,10 v10 q0,6 6,6 q-6,0 -6,6 v10 q0,10 -8,10" fill="none" stroke="#3f3f3f" stroke-width="1.5"/>
    <circle cx="80" cy="1073" r="54" fill="#b3b3b3"/>
    <circle cx="80" cy="1073" r="40" fill="#4d4d4d"/>
    <circle cx="430" cy="1073" r="52" fill="var(--white)"/>
    <circle cx="430" cy="1073" r="44" fill="#2e2e2e"/>
  </svg>

  <div class="abs brand-name">Wes Hadley<br>Golf</div>
  <div class="abs contact">whadley@fairwaymail.com<br>555-206-0199<br>whadleygolf.com</div>

  <h1 class="abs hero-title">GOLF<br>SWING<br>ANALYSIS</h1>
  <div class="abs hero-price">$59.<sup>99</sup></div>
  <div class="abs tag-hour">1-Hour<br>Analysis</div>
  <div class="abs tag-offer">*One-Time<br>limited offer<strong>REG.<br>$79.<sup>00</sup></strong></div>

  <h2 class="abs includes-title" style="top:484px">INCLUDES</h2>
  <ul class="abs feature-list">
    <li>Swing analysis with video</li>
    <li>Review of swing technique</li>
    <li>Suggested tips &amp; drills</li>
    <li>Video and summary sent to your mobile devices</li>
  </ul>

  <div class="abs info-cell" style="top:653px">Beginners to Advanced</div>
  <div class="abs info-cell" style="top:701px">Additional info<br><b>@www.whadleygolf.com</b></div>
  <div class="abs partner partner-swing">Swingly</div>
  <div class="abs partner partner-track">Trackwell</div>

  <h2 class="abs ribbon-text">SPECIAL LESSON PACKAGE</h2>
  <div class="abs package-line">3 One-Hour Lessons<span class="sep">|</span>Reg. $237.<sup>00</sup></div>
  <div class="abs package-price"><span class="amt">$225.<sup>00</sup></span><span class="note">(Limited deal)</span></div>
  <h3 class="abs includes-title package-sub">INCLUDES</h3>
  <ul class="abs package-list">
    <li>Video analysis</li>
    <li>Lesson summary and video review sent<br>to mobile devices</li>
    <li>Tips and drills</li>
    <li>Action plan to improve</li>
  </ul>
  <p class="abs footer-note">Wes Hadley class a member guarantee<br>Century member NLT</p>
</main>
</body>
</html>
```